New Business Card Design Project

Hi! I would like for you to design a business card for our aesthetic injections business. We offer Zelvia, filler, skin care. I would like it to be elegant, feminine, modern and sleek/clean. I like black/gold foil/ivory/parchment colors. It can be either one or two sided. I would like matte black with gold foil logo on one side and ivory with gold foil information on the other side

Target Market(s)

target market is the discerning woman who wants to look her best

Industry/Entity Type

beauty

Contact Information for Business Card

logo, name, phone, email, website, instagram, facebook, location

Requirements
Must have
• logo and info
Nice to have
• the icons for cell, instagram, email, fb etc
Should not have
• images of people

```html
<!DOCTYPE html>
<html lang="en">
<head>
<meta charset="utf-8">
<title>Velour Skin Lounge — Business Card</title>
<link rel="stylesheet" href="https://fonts.googleapis.com/css2?family=Open+Sans:ital,wght@0,400;0,700;1,400;1,600&family=Montserrat:wght@500&display=swap">
<style>
  :root {
    --backdrop: #dedede;
    --card: #07131d;
    --card-edge: #0b1a26;
    --gold: #cfa83f;
    --gold-soft: #b8922f;
  }
  * { box-sizing: border-box; margin: 0; padding: 0; }
  html, body {
    width: 1200px; height: 800px; overflow: hidden;
    background: var(--backdrop);
  }
  .canvas {
    position: relative; width: 1200px; height: 800px;
    display: flex; align-items: center; justify-content: center; gap: 50px;
  }
  .card {
    position: relative; width: 520px; height: 310px;
    border-radius: 44px;
    background: linear-gradient(135deg, var(--card-edge), var(--card) 60%);
    box-shadow: 0 18px 40px rgba(0,0,0,0.25);
    color: var(--gold);
    font-family: "Open Sans", sans-serif;
  }

  /* information side */
  .card-info__header {
    position: absolute; top: 44px; left: 44px;
    display: flex; align-items: center; gap: 18px;
  }
  .brand-mark {
    display: flex; align-items: center; gap: 8px;
    font-family: "Open Sans", sans-serif; font-size: 13px; font-weight: 400;
    color: var(--gold);
  }
  .brand-mark__dot {
    width: 14px; height: 14px; border-radius: 50%;
    border: 1.5px solid var(--gold);
  }
  .divider { width: 1.5px; height: 46px; background: var(--gold); transform: skewX(-20deg); }
  .person__name { font-weight: 700; font-size: 24px; letter-spacing: 0.5px; line-height: 1.1; }
  .person__role { font-style: italic; font-size: 15px; }

  .contact-list {
    position: absolute; top: 140px; left: 44px;
    list-style: none; display: flex; flex-direction: column; gap: 10px;
  }
  .contact-list__item {
    display: flex; align-items: center; gap: 12px;
    font-style: italic; font-size: 18px;
  }
  .contact-list__icon { width: 20px; height: 20px; flex: none; }
  .square-mark { width: 14px; height: 14px; background: var(--gold); border-radius: 2px; margin: 0 3px; }

  .address {
    position: absolute; right: 44px; bottom: 38px;
    display: flex; align-items: center; gap: 16px;
  }
  .address__text { font-style: italic; font-size: 13px; text-align: center; line-height: 1.35; }
  .address__icon { width: 18px; height: 24px; }

  /* logo side */
  .card-logo {
    display: flex; flex-direction: column; align-items: center; justify-content: center; gap: 22px;
  }
  .card-logo__mark {
    display: flex; align-items: center; gap: 14px;
    font-size: 34px; font-weight: 400; color: var(--gold);
  }
  .card-logo__ring {
    width: 26px; height: 26px; border-radius: 50%; border: 2px solid var(--gold);
  }
  .website {
    display: flex; align-items: center; gap: 10px;
    font-family: "Montserrat", sans-serif; font-weight: 500; font-size: 13px; letter-spacing: 1px;
  }
  .website__icon { width: 12px; height: 14px; }
</style>
</head>
<body>
<main class="canvas">

  <section class="card card-info" aria-label="Business card, contact side">
    <header class="card-info__header">
      <div class="brand-mark"><span class="brand-mark__dot"></span>Velour Skin Lounge</div>
      <span class="divider"></span>
      <div class="person">
        <p class="person__name">NAME SURNAME</p>
        <p class="person__role">Appellation</p>
      </div>
    </header>

    <ul class="contact-list">
      <li class="contact-list__item">
        <svg class="contact-list__icon" viewBox="0 0 24 24" aria-hidden="true">
          <path fill="var(--gold)" d="M6.6 10.8a15 15 0 0 0 6.6 6.6l2.2-2.2a1 1 0 0 1 1-.25 11.4 11.4 0 0 0 3.6.57 1 1 0 0 1 1 1V20a1 1 0 0 1-1 1A17 17 0 0 1 3 4a1 1 0 0 1 1-1h3.5a1 1 0 0 1 1 1c0 1.25.2 2.45.57 3.57a1 1 0 0 1-.25 1z"/>
        </svg>
        123 456 789 0
      </li>
      <li class="contact-list__item">
        <svg class="contact-list__icon" viewBox="0 0 24 24" aria-hidden="true">
          <rect x="2" y="5" width="20" height="14" rx="1.5" fill="var(--gold)"/>
          <path d="M2.5 6l9.5 7 9.5-7" fill="none" stroke="var(--card)" stroke-width="1.6"/>
        </svg>
        hello@velourskin.co
      </li>
      <li class="contact-list__item">
        <span class="contact-list__icon" style="display:flex;align-items:center"><span class="square-mark"></span></span>
        @velourskinlounge
      </li>
    </ul>

    <div class="address">
      <p class="address__text">your adrees<br>1121566</p>
      <svg class="address__icon" viewBox="0 0 18 24" aria-hidden="true">
        <path fill="var(--gold)" d="M9 0a8 8 0 0 0-8 8c0 6 8 16 8 16s8-10 8-16a8 8 0 0 0-8-8zm0 11a3 3 0 1 1 0-6 3 3 0 0 1 0 6z"/>
      </svg>
    </div>
  </section>

  <section class="card card-logo" aria-label="Business card, logo side">
    <div class="card-logo__mark"><span class="card-logo__ring"></span>Velour Skin Lounge</div>
    <div class="website">
      <svg class="website__icon" viewBox="0 0 12 14" aria-hidden="true">
        <path fill="var(--gold)" d="M0 0l11 8-4.5.6L9 13l-1.8.9-2.4-4.4L1.5 12.5z"/>
      </svg>
      www websiteaddress
    </div>
  </section>

</main>
</body>
</html>
```